Business Cards and Logo needed for Rum Website

I need a smart, modern but fun business card (and Logo) to help promote my website BrightBarrelNotes.com

The website contains reviews of Rum (and eventually other spirits) as well as news and blog posts.

I would like a 2-sided design, with the logo and company name on one side and text on the other.

Text fields required are:
Name (Dan Fowler)
Website (www.brightbarrelnotes.com)
Email (dan@brightbarrelnotes.com)
Twitter (@BrightBarrelNotes)

For the logo i'm open to suggestions however it must incorporate a wooden Cask and a number of Stars. Ideas so far have been for a Cask surrounded in a number of Stars forming a circle around it with the text Bright Barrel Notes underneath. The logo should be modern but also a little bit cartoony and stylised. General drink/spirits themes will also be considered.

Colours: I like the idea of yellow text with black background but again i'm open to suggestions on what would work well. Contrasting colours for the 2-sides would be good.

Cards will be printed via Pelv.com so please consult their style guidelines if required: http://uk.pelv.com/help/faq/templates-and-guidelines.html

Requirements
Must have
• A spirits Cask
A number of Stars (preferrably yellow or gold)

```html
<!DOCTYPE html>
<html lang="en">
<head>
<meta charset="utf-8">
<title>Bright Barrel Notes — Business Card</title>
<link rel="stylesheet" href="https://fonts.googleapis.com/css2?family=Poiret+One&display=swap">
<style>
  :root {
    --page-cream: #fff1d8;
    --front-brown: #33261a;
    --front-ring: #4e3d2c;
    --star-gold: #e3cf91;
    --back-taupe: #9b8b79;
    --back-band: #b1a290;
    --back-text: #ece3d5;
    --back-text-soft: #ddd1bf;
    --back-circle: rgba(255, 255, 255, 0.14);
    --back-mark-text: rgba(255, 255, 255, 0.32);
  }
  html, body {
    margin: 0;
    padding: 0;
    width: 1051px;
    height: 1200px;
    overflow: hidden;
    background: var(--page-cream);
    font-family: "Poiret One", sans-serif;
  }
  .canvas {
    position: relative;
    width: 1051px;
    height: 1200px;
  }
  .card {
    position: absolute;
    left: 119px;
    width: 823px;
    height: 469px;
    border-radius: 35px;
    overflow: hidden;
  }
  .card--front {
    top: 96px;
    background: var(--front-brown);
  }
  .card--back {
    top: 609px;
    background: var(--back-taupe);
  }
  .brand {
    position: absolute;
    left: 0;
    right: 0;
    top: 205px;
    display: flex;
    align-items: center;
    justify-content: center;
    gap: 22px;
    color: var(--star-gold);
    font-size: 56px;
    letter-spacing: 1px;
  }
  .brand__dot {
    width: 34px;
    height: 34px;
    border-radius: 50%;
    background: var(--star-gold);
    flex: none;
  }
  .back-circle {
    position: absolute;
    left: 450px;
    top: -32px;
    width: 530px;
    height: 530px;
    border-radius: 50%;
    background: var(--back-circle);
  }
  .back-brand {
    position: absolute;
    left: 470px;
    top: 230px;
    width: 353px;
    text-align: center;
    color: var(--back-mark-text);
    font-size: 38px;
  }
  .contact {
    position: absolute;
    left: 35px;
    top: 200px;
    color: var(--back-text);
  }
  .contact__name {
    font-size: 54px;
    margin: 0 0 18px;
    font-weight: 400;
  }
  .contact__line {
    font-size: 31px;
    margin: 0 0 14px;
    color: var(--back-text-soft);
  }
  .web-band {
    position: absolute;
    left: 0;
    right: 0;
    bottom: 0;
    height: 66px;
    background: var(--back-band);
    display: flex;
    align-items: center;
    padding-left: 38px;
    color: var(--back-text-soft);
    font-size: 35px;
  }
</style>
</head>
<body>
  <main class="canvas">
    <section class="card card--front" aria-label="Card front">
      <div class="brand">
        <span class="brand__dot"></span>
        <span class="brand__name">Bright Barrel Notes</span>
      </div>
    </section>

    <section class="card card--back" aria-label="Card back">
      <div class="back-circle"></div>
      <div class="back-brand">Bright Barrel Notes</div>
      <div class="contact">
        <h1 class="contact__name">Dan Fowler</h1>
        <p class="contact__line">dan@brightbarrelnotes.com</p>
        <p class="contact__line">Twitter: @BrightBarrelNotes</p>
      </div>
      <div class="web-band">www.brightbarrelnotes.com</div>
    </section>
  </main>
</body>
</html>
```